Website design for headhunting agency

The design I need (PSD file) is for a company offering specialised services in recruitment of high-end executive and management positions for businesses.
OBJECTIVES OF THE WEBSITE:
1. Let entrepreneurs and business leaders know about their services and easily have them contact Velnarix if they want more information about their services.
2. Display a list of available carreer opportunities (according to their client's need).
WHAT I NEED:
1st, I need the design for the Home Page ONLY. Once approved, I will need the other pages designed as well. (Here is prototype that we've already developed for the Website that will guide you in the design:
http://demo.quorvaweb.example/velnarix/fr/accueil)
ATTACHED FILES
- Logo
- PDF brochure: Use for inspiration. It is encouraged that you use pictures from this brochure. You can always suggest new ones, as long as they are not expensive to buy and have the same look and feel as the brochure.
HOMEPAGE:
1. Main menu : 6 sections
Accueil | Velnarix | Équipe | Approche | Postes disponibles | Publications
2. Main slider: 4 sections
- Chasseurs de têtes (Headhunters)
- Notre approche (Our Approach)
- Postes cadres disponibles (Executive Careers
Opportunities)
- Contactez-nous (Contact Us)
3. Main Call To Action Boxes :
- Liste Des postes disponibles (Liste of Available Careers
Opportunities)
- Formulaire de contact (contact form)
4. Latest blog articles
- Les derniers articles.
OTHER PAGES (to design once Homepage is approved)
- Velnarix (about us)
- Équipe (our team)
- Approche (our approach)
- Postes disponibles (Career opportunities)
- Publications (blog articles)
- Contact (Contact us)
Target Market(s)
ORGANIZATIONS:
Leaders of organizations seeking to recruit highly qualified staff.
HIGHLY QUALIFIED RESOURCES:
Senior individuals seeking a salary between $70,000 and $ $200,000 annually
PROFESSIONAL SECTORS:
manufacturing : Primary and secondary industries
pharmaceutical
Aerospace
Finances
Retail business
Engineering
Chemical and petrochemical
IT, telecommunications and high technology
Professional Organizations and Association
Industry/Entity Type
Business
Look and feel
Each slider illustrates characteristics of the customer's brand and the style your logo design should communicate.

```html
<!DOCTYPE html>
<html lang="fr">
<head>
<meta charset="utf-8">
<title>Velnarix – Recherche de cadres</title>
<link href="https://fonts.googleapis.com/css2?family=Open+Sans:wght@400;600;700&display=swap" rel="stylesheet">
<style>
:root{
  --teal-dark:#0b4a52;
  --teal:#1a6f7a;
  --teal-mid:#3f8d8f;
  --teal-pale:#c2d9d1;
  --orange:#e8a33a;
  --ink:#222;
  --grey-text:#9a9a9a;
  --line:#cfd8d8;
  --white:#fff;
  --btn:#1b1b1b;
}
*{box-sizing:border-box;margin:0;padding:0}
html,body{width:703px;height:1200px;overflow:hidden;background:var(--white);font-family:"Open Sans",Arial,sans-serif;color:var(--ink)}
.page{position:relative;width:703px;height:1200px}
.topbar{position:absolute;left:0;top:0;width:703px;height:21px;background:linear-gradient(var(--teal),var(--teal-dark));display:flex;justify-content:flex-end}
.topbar a{color:var(--white);font-size:10px;font-weight:600;letter-spacing:.5px;text-decoration:none;line-height:21px;text-align:center;border-left:1px solid rgba(255,255,255,.35)}
.topbar a:first-child{border-left:none}
.brand{position:absolute;left:16px;top:44px}
.brand-name{font-size:35px;font-weight:600;color:var(--teal);letter-spacing:1px;line-height:1}
.brand-tag{font-size:11px;color:#555;margin-left:66px;margin-top:2px}
.mainnav{position:absolute;right:12px;top:62px;display:flex;font-size:11.5px;font-weight:600;letter-spacing:.4px}
.mainnav a{color:var(--teal);text-decoration:none;padding:0 11px;border-left:1px solid #aaa;line-height:13px}
.mainnav a:first-child{border-left:none}
.mainnav a.current{color:var(--orange)}
.header-rule{position:absolute;left:0;top:109px;width:703px;height:1px;background:var(--line)}
.slider{position:absolute;left:0;top:112px;width:703px;height:272px;overflow:hidden}
.slide-photo{position:absolute;left:0;top:0;width:703px;height:272px;background:linear-gradient(90deg,#e9eeee 40%,#c9ced3 70%,#f3f3f3)}
.slide-panel{position:absolute;left:0;top:0}
.slide-title{position:absolute;left:41px;top:64px;font-size:22px;font-weight:600;color:var(--teal-dark);letter-spacing:.5px}
.slide-text{position:absolute;left:46px;top:105px;width:210px;font-size:10.5px;line-height:16px;color:var(--white)}
.slide-arrow{position:absolute;top:122px}
.btn{display:inline-flex;align-items:center;gap:5px;height:22px;padding:0 9px;background:var(--btn);color:var(--white);font-size:10.5px;font-weight:600;border-radius:4px;text-decoration:none}
.btn svg{width:8px;height:8px}
.btn-light{background:var(--teal);border:1px solid var(--white);position:absolute;left:41px;top:211px;height:24px;font-size:11px}
.dots{position:absolute;left:322px;top:400px;display:flex;gap:5px}
.dots span{width:10px;height:10px;border-radius:50%;background:#c8c8c8}
.dots span.on{background:var(--teal)}
.box{position:absolute;top:432px;height:191px;border:1px solid var(--line)}
.box h2{position:absolute;left:9px;top:14px;font-size:13px;font-weight:400;letter-spacing:.4px}
.jobs{position:absolute;left:15px;top:44px;list-style:none}
.jobs li{font-size:10.5px;color:var(--teal);line-height:16.5px;display:flex;align-items:center;gap:10px}
.jobs li::before{content:"";border-left:7px solid var(--ink);border-top:3.5px solid transparent;border-bottom:3.5px solid transparent}
.box-jobs{left:15px;width:328px}
.box-jobs .btn{position:absolute;left:29px;top:154px}
.box-contact{left:359px;width:329px;background:var(--teal-pale);border:none}
.field{position:absolute;left:35px;display:flex;align-items:center;font-size:11.5px;color:var(--teal-dark)}
.field span{width:92px}
.field i{display:block;width:166px;height:21px;background:var(--white)}
.box-contact .btn{position:absolute;left:35px;top:153px;width:76px}
.section-rule{position:absolute;left:0;top:640px;width:703px;height:1px;background:var(--line)}
.section-title{position:absolute;left:24px;top:651px;font-size:13px;font-weight:400;letter-spacing:.4px}
.card{position:absolute;width:328px;height:190px;border:1px solid var(--line)}
.card-photo{position:absolute;left:11px;top:11px;width:120px;height:78px;border:1px solid #ddd}
.card-intro{position:absolute;left:144px;top:11px;width:172px;font-size:8.6px;line-height:14.5px;color:var(--grey-text)}
.card-body{position:absolute;left:9px;top:101px;width:312px;font-size:8.6px;line-height:14.5px;color:var(--grey-text)}
.card .btn{position:absolute;left:9px;top:156px}
.follow{position:absolute;top:1104px;display:flex;align-items:center;gap:8px;font-size:12.5px;letter-spacing:.3px}
.follow::before{content:"";border-left:6px solid var(--ink);border-top:3px solid transparent;border-bottom:3px solid transparent}
.badge{display:inline-block;margin-left:6px;padding:0 10px;height:32px;line-height:30px;border:1px solid var(--line);font-size:15px;font-weight:700;color:var(--ink)}
.badge-sign{color:var(--teal-dark);padding:0 14px}
.footer{position:absolute;left:0;top:1171px;width:703px;height:29px;background:linear-gradient(var(--teal),var(--teal-dark));color:var(--white);font-size:9.5px;line-height:29px;padding:0 25px;display:flex;justify-content:space-between}
</style>
</head>
<body>
<div class="page">
  <nav class="topbar">
    <a href="#" style="width:75px">ACCUEIL</a>
    <a href="#" style="width:98px">PLAN DU SITE</a>
    <a href="#" style="width:127px">CODE D'ÉTIQUE</a>
    <a href="#" style="width:105px">CONTACT</a>
    <a href="#" style="width:93px">ENGLISH</a>
  </nav>

  <div class="brand">
    <div class="brand-name">VELNARIX</div>
    <div class="brand-tag">Recherche de cadres</div>
  </div>

  <nav class="mainnav">
    <a href="#" class="current">À PROPOS</a>
    <a href="#">ÉQUIPE</a>
    <a href="#">APPROCHE</a>
    <a href="#">POSTES DISPONIBLES</a>
    <a href="#">PUBLICATIONS</a>
  </nav>
  <div class="header-rule"></div>

  <section class="slider">
    <div class="slide-photo" role="img" aria-label="Photo d'une équipe de cadres souriants en tenue d'affaires"></div>
    <svg class="slide-panel" width="330" height="272" viewBox="0 0 330 272">
      <polygon points="0,0 320,0 262,272 0,272" fill="#5b9a9a"/>
      <polygon points="250,0 320,0 262,272 240,272" fill="#7fb3b0" opacity=".7"/>
      <polygon points="0,0 230,0 180,272 0,272" fill="#4f8f90" opacity=".5"/>
    </svg>
    <h1 class="slide-title">CHASSEURS DE TÊTES</h1>
    <p class="slide-text">Donec quam felis, ultricies nec, pellentesque eu, pretium quis, sem. Nulla consequat massa quis enim. Donec pede justo, fringilla vel, aliquet nec, vulputate eget, arcu. In enim justo, rhoncus ut, imperdiet a, venenatis vitae, justo.</p>
    <a href="#" class="btn btn-light"><svg viewBox="0 0 8 8"><polygon points="1,0 8,4 1,8" fill="#fff"/></svg>View More</a>
    <svg class="slide-arrow" style="left:6px" width="14" height="20" viewBox="0 0 14 20"><polyline points="11,2 3,10 11,18" fill="none" stroke="#cfd9d9" stroke-width="4"/></svg>
    <svg class="slide-arrow" style="right:6px" width="14" height="20" viewBox="0 0 14 20"><polyline points="3,2 11,10 3,18" fill="none" stroke="#5b9a9a" stroke-width="4"/></svg>
  </section>
  <div class="dots"><span class="on"></span><span></span><span></span><span></span></div>

  <section class="box box-jobs">
    <h2>LISTE DES POSTES DISPONIBLES</h2>
    <ul class="jobs">
      <li>Aonecqua mfelisuame</li>
      <li>Bonecqua mfeluame</li>
      <li>Conecqua mame</li>
      <li>Doneiua feuame</li>
      <li>Enecqua rhlisuame</li>
      <li>FAonecqua yrelisume</li>
    </ul>
    <a href="#" class="btn"><svg viewBox="0 0 8 8"><polygon points="1,0 8,4 1,8" fill="#fff"/></svg>View More</a>
  </section>

  <section class="box box-contact">
    <h2>FORMULAIRE DE CONTACT</h2>
    <div class="field" style="top:52px"><span>User Name</span><i></i></div>
    <div class="field" style="top:96px"><span>Password</span><i></i></div>
    <a href="#" class="btn"><svg viewBox="0 0 8 8"><polygon points="1,0 8,4 1,8" fill="#fff"/></svg>&nbsp;Login</a>
  </section>

  <div class="section-rule"></div>
  <h2 class="section-title">LES DERNIERS ARTICLES</h2>

  <article class="card" style="left:15px;top:676px">
    <div class="card-photo" role="img" aria-label="Photo de collègues en réunion autour d'un ordinateur" style="background:linear-gradient(135deg,#d9dcdc,#8b6f63 60%,#e4e4e4)"></div>
    <p class="card-intro">Donec quam felis, ultricies nec, pellentesque eu, pretium quis, sem. Nulla consequat massa quis enim. Donec pede justo, fringilla vel, aliquet nec, vulputate eget, arcu.</p>
    <p class="card-body">Donec quam felis, ultricies nec, pellentesque eu, pretium quis, sem. Nulla consequat massa quis enim. Donec pede justo, fringilla vel, aliquet nec, vulputate eget, arcu.</p>
    <a href="#" class="btn"><svg viewBox="0 0 8 8"><polygon points="1,0 8,4 1,8" fill="#fff"/></svg>View More</a>
  </article>
  <article class="card" style="left:359px;top:676px">
    <div class="card-photo" role="img" aria-label="Photo de plans roulés et de documents techniques" style="background:linear-gradient(135deg,#f3f5f6,#c9d3db)"></div>
    <p class="card-intro">Donec quam felis, ultricies nec, pellentesque eu, pretium quis, sem. Nulla consequat massa quis enim. Donec pede justo, fringilla vel, aliquet nec, vulputate eget, arcu.</p>
    <p class="card-body">Donec quam felis, ultricies nec, pellentesque eu, pretium quis, sem. Nulla consequat massa quis enim. Donec pede justo, fringilla vel, aliquet nec, vulputate eget, arcu.</p>
    <a href="#" class="btn"><svg viewBox="0 0 8 8"><polygon points="1,0 8,4 1,8" fill="#fff"/></svg>View More</a>
  </article>
  <article class="card" style="left:15px;top:885px">
    <div class="card-photo" role="img" aria-label="Photo d'une entrevue entre deux professionnels" style="background:linear-gradient(135deg,#e9e2da,#8a5a45 55%,#ddd)"></div>
    <p class="card-intro">Donec quam felis, ultricies nec, pellentesque eu, pretium quis, sem. Nulla consequat massa quis enim. Donec pede justo, fringilla vel, aliquet nec, vulputate eget, arcu.</p>
    <p class="card-body">Donec quam felis, ultricies nec, pellentesque eu, pretium quis, sem. Nulla consequat massa quis enim. Donec pede justo, fringilla vel, aliquet nec, vulputate eget, arcu.</p>
    <a href="#" class="btn"><svg viewBox="0 0 8 8"><polygon points="1,0 8,4 1,8" fill="#fff"/></svg>View More</a>
  </article>
  <article class="card" style="left:359px;top:885px">
    <div class="card-photo" role="img" aria-label="Photo de gens d'affaires dans un bureau lumineux" style="background:linear-gradient(135deg,#eef1f1,#7d8a8e 55%,#e6ebeb)"></div>
    <p class="card-intro">Donec quam felis, ultricies nec, pellentesque eu, pretium quis, sem. Nulla consequat massa quis enim. Donec pede justo, fringilla vel, aliquet nec, vulputate eget, arcu.</p>
    <p class="card-body">Donec quam felis, ultricies nec, pellentesque eu, pretium quis, sem. Nulla consequat massa quis enim. Donec pede justo, fringilla vel, aliquet nec, vulputate eget, arcu.</p>
    <a href="#" class="btn"><svg viewBox="0 0 8 8"><polygon points="1,0 8,4 1,8" fill="#fff"/></svg>View More</a>
  </article>

  <div class="follow" style="left:22px">SUIVEZ-NOUS SUR LINKORA <span class="badge">Linkora</span></div>
  <div class="follow" style="left:366px">INSCRIVEZ-VOUS À L'INFOLETTRE <span class="badge badge-sign">Sign Up</span></div>

  <footer class="footer">
    <span>© Velnarix – Tous droits réservés</span>
    <span>Site Web et stratégie Agence de Développement Internet</span>
  </footer>
</div>
</body>
</html>
```